Verpackungsdesign für Kaffeerösterei
Zielgruppe
wir Rösten Kaffee. Wir haben uns darauf Spezialisiert Hochwertigen Premium Caffe Crema herzustellen und bieten auch nur diesen in Unserem Shop www.brunor7-kaffee.de an. wir bieten 250gr. 500gr. Kaffee an. .
Es kann gerne verrückt oder anders sein, dennoch aber sehr edel.
die Zielgruppe ist weitgestreut, aber laut unserern Daten ist die Ideale Zielgruppe der 52 Jährige Mann, der Wert auf Hochwertige Genussmittel legt und auch bereit ist mehr Geld dafür zu bezahlen.
ich habe bereits ein beispiel design und die Druckvorlage bereitgestellt.
Aufgabenstellung
das Konzept unserer Internetseite sollte berücksichtigt werden, ansonsten ist dem Kreativen kopf keine Grenzen gesetzt.

```html
<!DOCTYPE html>
<html lang="de">
<head>
<meta charset="utf-8">
<title>Korvane – Cafe Crema Verpackung</title>
<link rel="stylesheet" href="https://fonts.googleapis.com/css2?family=Cormorant+Garamond:wght@500;700&family=Stint+Ultra+Condensed&display=swap">
<style>
  :root {
    --backdrop: #d9d9d9;
    --bag-black: #141110;
    --bag-edge: #0a0807;
    --seal-line: #2a2522;
    --gold: #d4a01e;
    --copper: #a8714c;
    --ground-dark: #2a150c;
    --ground-mid: #4a2716;
    --bean-dark: #1c120d;
    --bean-mid: #3b2419;
    --stamp-gold: #b8912f;
    --stamp-rim: #1a1410;
  }
  * { margin: 0; padding: 0; box-sizing: border-box; }
  html, body {
    width: 849px;
    height: 1200px;
    overflow: hidden;
    background: var(--backdrop);
  }
  .canvas {
    position: relative;
    width: 849px;
    height: 1200px;
  }
  .bag {
    position: absolute;
    left: 168px;
    top: 175px;
    width: 510px;
    height: 978px;
    background: linear-gradient(180deg, #1b1716 0%, var(--bag-black) 30%, var(--bag-edge) 100%);
    overflow: hidden;
  }
  .seal-lines {
    position: absolute;
    left: 0;
    top: 10px;
    width: 100%;
    height: 40px;
  }
  .brand-name {
    position: absolute;
    left: 0;
    top: 196px;
    width: 100%;
    text-align: center;
    font-family: "Cormorant Garamond", serif;
    font-weight: 700;
    font-size: 40px;
    line-height: 1;
    letter-spacing: 3px;
    color: var(--gold);
  }
  .brand-mark {
    display: inline-block;
    width: 12px;
    height: 12px;
    margin-left: 10px;
    border-radius: 50%;
    background: var(--gold);
    vertical-align: middle;
  }
  .beans-band {
    position: absolute;
    left: 0;
    top: 225px;
    width: 100%;
    height: 400px;
  }
  .ground-panel {
    position: absolute;
    left: 50px;
    top: 465px;
    width: 404px;
    height: 513px;
    background: radial-gradient(ellipse at 60% 70%, var(--ground-mid) 0%, var(--ground-dark) 75%);
  }
  .stamp {
    position: absolute;
    left: 316px;
    top: 368px;
    width: 140px;
    height: 140px;
  }
  .product-title {
    position: absolute;
    left: 0;
    top: 512px;
    width: 100%;
    text-align: center;
    font-family: "Stint Ultra Condensed", serif;
    font-weight: 400;
    font-size: 86px;
    line-height: 1;
    letter-spacing: 2px;
    color: var(--copper);
  }
  .blend,
  .acidity,
  .net-weight {
    position: absolute;
    left: 0;
    width: 100%;
    text-align: center;
    font-family: "Cormorant Garamond", serif;
    font-weight: 500;
    font-variant-numeric: lining-nums;
    color: var(--copper);
  }
  .blend {
    top: 601px;
    font-size: 21px;
    line-height: 24px;
  }
  .acidity {
    top: 676px;
    font-size: 21px;
    line-height: 24px;
  }
  .net-weight {
    top: 906px;
    font-size: 29px;
    line-height: 34px;
  }
</style>
</head>
<body>
<div class="canvas">
  <div class="bag">
    <svg class="seal-lines" viewBox="0 0 510 40" preserveAspectRatio="none" aria-hidden="true">
      <g stroke="var(--seal-line)" stroke-width="1">
        <line x1="250" y1="6" x2="510" y2="6"/>
        <line x1="250" y1="14" x2="510" y2="14"/>
        <line x1="250" y1="22" x2="510" y2="22"/>
        <line x1="250" y1="30" x2="510" y2="30"/>
      </g>
    </svg>

    <svg class="beans-band" viewBox="0 0 510 400" preserveAspectRatio="none" role="img" aria-label="Fotografie gerösteter Kaffeebohnen">
      <defs>
        <linearGradient id="beanTone" x1="0" y1="0" x2="0" y2="1">
          <stop offset="0" stop-color="var(--bean-mid)"/>
          <stop offset="0.6" stop-color="var(--bean-dark)"/>
          <stop offset="1" stop-color="var(--bag-black)"/>
        </linearGradient>
      </defs>
      <path d="M0 40 C60 10 120 60 200 65 C280 70 360 55 420 30 C460 15 490 5 510 0 L510 250 C470 240 430 235 400 240 C340 260 260 300 160 290 C90 280 40 270 0 260 Z" fill="url(#beanTone)"/>
    </svg>

    <div class="ground-panel" role="img" aria-label="Fotografie von gemahlenem Kaffee"></div>

    <svg class="stamp" viewBox="0 0 140 140" aria-hidden="true">
      <circle cx="70" cy="70" r="68" fill="var(--stamp-rim)"/>
      <circle cx="70" cy="70" r="62" fill="var(--stamp-gold)"/>
    </svg>

    <div class="brand-name">KORVANE<span class="brand-mark"></span></div>

    <h1 class="product-title">CAFE CREMA</h1>
    <p class="blend">70% Robusta<br>30% Hochland Arabica</p>
    <p class="acidity">Säurearm</p>
    <p class="net-weight">Net wt. 500g</p>
  </div>
</div>
</body>
</html>
```